Dune Air & Plus business card

I need an awesome, double-sided business card designed with our new logo. I would like the one side black with the colored logo, and the back side is all yours. I'd like to see horizontal and vertical layouts. Get creative! Thank you.

Target Market(s)

HVAC, Heating and Cooling in Phoenix, AZ

Industry/Entity Type

HVAC

Contact Information for Business Card

We need our new logo on the card. Tom Harker, (623) 555-0142, tom@trydunesair.com, www.trydunesair.com, ROC 514273

```html
<!DOCTYPE html>
<html lang="en">
<head>
<meta charset="utf-8">
<title>Dune Air &amp; Plus — Business Card</title>
<link href="https://fonts.googleapis.com/css2?family=Montserrat:wght@400;600;800&display=swap" rel="stylesheet">
<style>
  :root {
    --backdrop: #3b3b3b;
    --card: #141414;
    --edge-blue: #1f7fd6;
    --name-blue: #2c86dc;
    --accent-orange: #f0772a;
    --text-light: #e9e9e9;
    --emboss: #2a2a2a;
  }
  html, body {
    margin: 0;
    width: 1200px;
    height: 801px;
    overflow: hidden;
    background: var(--backdrop);
    font-family: "Montserrat", sans-serif;
  }
  .stage {
    position: relative;
    width: 1200px;
    height: 801px;
    display: flex;
    align-items: center;
    justify-content: center;
    gap: 40px;
  }
  .card {
    position: relative;
    width: 540px;
    height: 309px;
    background: var(--card);
    border-bottom: 3px solid var(--edge-blue);
    box-sizing: border-box;
  }
  .card-front {
    display: flex;
    align-items: center;
  }
  .brand {
    width: 245px;
    display: flex;
    align-items: center;
    justify-content: center;
    gap: 10px;
  }
  .brand-dot {
    width: 16px;
    height: 16px;
    border-radius: 50%;
    background: var(--accent-orange);
    flex: none;
  }
  .brand-name {
    font-weight: 800;
    font-size: 24px;
    color: var(--name-blue);
    letter-spacing: 0.5px;
    line-height: 1.1;
  }
  .divider {
    width: 1px;
    height: 150px;
    background: var(--edge-blue);
  }
  .contact {
    padding-left: 30px;
    color: var(--text-light);
  }
  .person-name {
    margin: 0;
    font-weight: 600;
    font-size: 20px;
    color: var(--name-blue);
    letter-spacing: 0.5px;
  }
  .licence {
    margin: 4px 0 22px;
    font-size: 14px;
  }
  .contact-list {
    list-style: none;
    margin: 0;
    padding: 0;
    font-size: 14px;
  }
  .contact-list li {
    display: flex;
    align-items: center;
    gap: 10px;
    margin-bottom: 8px;
  }
  .contact-icon { width: 14px; height: 14px; flex: none; }
  .card-back {
    display: flex;
    align-items: center;
    justify-content: center;
  }
  .back-mark {
    font-weight: 800;
    font-size: 46px;
    color: var(--emboss);
    letter-spacing: 1px;
  }
</style>
</head>
<body>
<main class="stage">
  <section class="card card-front">
    <div class="brand">
      <span class="brand-dot"></span>
      <span class="brand-name">Dune Air<br>&amp; Plus</span>
    </div>
    <div class="divider"></div>
    <div class="contact">
      <h1 class="person-name">TOM HARKER</h1>
      <p class="licence">ROC 514273</p>
      <ul class="contact-list">
        <li>
          <svg class="contact-icon" viewBox="0 0 16 16" aria-hidden="true"><path fill="#f0772a" d="M3 1l3 3-2 2c1 2 3 4 5 5l2-2 3 3-2 3C7 15 1 9 1 3z"/></svg>
          (623) 555-0142
        </li>
        <li>
          <svg class="contact-icon" viewBox="0 0 16 16" aria-hidden="true"><rect x="1" y="3" width="14" height="10" fill="#f0772a"/><path d="M1 3l7 6 7-6" fill="none" stroke="#141414" stroke-width="1.4"/></svg>
          tom@trydunesair.com
        </li>
        <li>
          <svg class="contact-icon" viewBox="0 0 16 16" aria-hidden="true"><circle cx="8" cy="8" r="7" fill="#f0772a"/><path d="M1 8h14M8 1c-3 4-3 10 0 14M8 1c3 4 3 10 0 14" fill="none" stroke="#141414" stroke-width="1.2"/></svg>
          www.trydunesair.com
        </li>
      </ul>
    </div>
  </section>
  <section class="card card-back">
    <span class="back-mark">Dune Air &amp; Plus</span>
  </section>
</main>
</body>
</html>
```